Business Card Design Project

I am an aviation professional (corporate pilot), and am looking to market myself to the business jet operators for short term crew leasing. The card should have name and contact info on the front side; qualifications, licenses held and type ratings on the back side.
Company name is: Harbinvale Skyline Partners Inc.
Updates

Sorry for the delay. will reply in another day or two.
best regards,

P

Target Market(s)

Business Jet Management companies and private jet operators

Industry/Entity Type

Business

Requirements
Must have
• It needs to be an aviation inspired design.

```html
<!DOCTYPE html>
<html lang="en">
<head>
<meta charset="utf-8">
<title>Harbinvale Skyline Partners Inc. — Business Card</title>
<link rel="stylesheet" href="https://fonts.googleapis.com/css2?family=Open+Sans:ital,wght@0,400;0,600;0,800;1,400&family=Cormorant+Garamond:wght@500&display=swap">
<style>
  :root {
    --stage: #cfcfcf;
    --stage-light: #e4e4e4;
    --card-black: #050505;
    --card-silver: #e9e9e9;
    --card-silver-edge: #bdbdbd;
    --ink-white: #ffffff;
    --ink-soft: #d8d8d8;
    --ink-dark: #1a1a1a;
    --ink-faint: #a9a9a9;
    --label: #3a3a3a;
  }
  * { margin: 0; padding: 0; box-sizing: border-box; }
  html, body { width: 1200px; height: 765px; overflow: hidden; }
  body {
    position: relative;
    background: linear-gradient(180deg, var(--stage-light) 0%, var(--stage) 100%);
    font-family: "Open Sans", sans-serif;
  }
  .card {
    position: absolute;
    top: 302px;
    width: 575px;
    height: 344px;
    border-radius: 34px;
    overflow: hidden;
  }
  .card--front { left: 17px; background: var(--card-black); color: var(--ink-white); }
  .card--back {
    left: 609px;
    background: radial-gradient(ellipse at 45% 30%, #fbfbfb 0%, var(--card-silver) 45%, var(--card-silver-edge) 100%);
    color: var(--ink-dark);
  }
  .card__art { position: absolute; inset: 0; width: 100%; height: 100%; }
  .brand {
    position: absolute;
    display: flex;
    align-items: center;
    gap: 12px;
    font-weight: 800;
    text-transform: uppercase;
    color: var(--ink-white);
  }
  .brand__mark { background: var(--ink-white); flex: none; }
  .brand__name { line-height: 1.05; }
  .brand--front { left: 36px; top: 76px; font-size: 24px; }
  .brand--front .brand__mark { width: 40px; height: 40px; }
  .holder {
    position: absolute;
    right: 39px;
    top: 155px;
    text-align: right;
  }
  .holder__name { font-size: 22px; font-weight: 600; line-height: 1.2; }
  .holder__role { font-size: 11.5px; letter-spacing: 0.6px; color: var(--ink-soft); }
  .contact {
    position: absolute;
    right: 39px;
    top: 212px;
    text-align: right;
    font-size: 11.5px;
    line-height: 16px;
  }
  .contact__address { margin-bottom: 12px; }
  .quals {
    position: absolute;
    left: 0; right: 0;
    top: 100px;
    text-align: center;
    font-size: 18px;
    line-height: 23px;
    letter-spacing: 0.5px;
  }
  .quals em { font-style: italic; }
  .brand--faint {
    left: 50%;
    top: 232px;
    transform: translateX(-50%);
    font-size: 19px;
    color: var(--ink-faint);
    white-space: nowrap;
  }
  .brand--faint .brand__mark { width: 32px; height: 32px; background: var(--ink-faint); }
  .side-label {
    position: absolute;
    top: 684px;
    font-family: "Cormorant Garamond", serif;
    font-size: 15px;
    letter-spacing: 3px;
    color: var(--label);
  }
  .side-label--front { left: 66px; }
  .side-label--back { left: 660px; }
</style>
</head>
<body>
  <section class="card card--front">
    <svg class="card__art" viewBox="0 0 575 344" role="img" aria-label="Abstract chrome shard decoration">
      <defs>
        <linearGradient id="chrome" x1="0" y1="0" x2="1" y2="1">
          <stop offset="0" stop-color="#2a2a2a"/>
          <stop offset="0.45" stop-color="#bcbcbc"/>
          <stop offset="0.7" stop-color="#3a3a3a"/>
          <stop offset="1" stop-color="#9a9a9a"/>
        </linearGradient>
      </defs>
      <polygon points="210,0 575,0 575,160 500,120" fill="url(#chrome)" opacity="0.85"/>
      <polygon points="0,270 230,344 0,344" fill="url(#chrome)" opacity="0.7"/>
    </svg>
    <div class="brand brand--front">
      <span class="brand__mark"></span>
      <span class="brand__name">Harbinvale Skyline<br>Partners Inc.</span>
    </div>
    <div class="holder">
      <div class="holder__name">Laurent Vaillancourt</div>
      <div class="holder__role">Captain</div>
    </div>
    <div class="contact">
      <div class="contact__address">58 Ridgemere Road North, Oakdale, ON, K4R1T7 Canada</div>
      <div>Tel.: +971 50 5550142 (M) &nbsp;|&nbsp; +1 905 555 0187 (H)</div>
      <div>Chat: laurent-vaillancourt</div>
      <div>email: laurent.vaillancourt@example.com</div>
      <div>Profile: Laurent Vaillancourt</div>
    </div>
  </section>

  <section class="card card--back">
    <div class="quals">
      <div><em>Licenses:</em> ATPL: FAA &amp; Transport Canada</div>
      <div><em>Type Ratings:</em> Norvane Stratus S-640/650</div>
      <div>Norvane Kestrel K-62LR</div>
      <div>Aldermoor AM-740/BX</div>
      <div>Veyra Aero V-32</div>
    </div>
    <div class="brand brand--faint">
      <span class="brand__mark"></span>
      <span class="brand__name">Harbinvale Skyline<br>Partners Inc.</span>
    </div>
  </section>

  <div class="side-label side-label--front">FRONT</div>
  <div class="side-label side-label--back">BACK</div>
</body>
</html>
```